Medical Practice Business Card

we need a business card for our new medical ophthalmology practice based in Needham Massachusetts. we are looking for a simple , modern and elegant design.
the card needs to contain the following
1- the logo of our practice (please see attached file)
2- the name of the practice : "Silver Birch Retina Care"
3- Doctor's Name: Tobias Rendell MD PhD
4- Specialty: Board-Certified Vitreoretinal Surgeon
5- practice address: 87 Larkspur Ave, Suite 210, Fernbrook ME 04412
7- Office number: 617- 482 - 7730
8- fax number: 617- 391 - 2268
9- email: info@sbretinahub.example
10- website: www.sbretinahub.example

```html
<!DOCTYPE html>
<html lang="en">
<head>
<meta charset="utf-8">
<title>Silver Birch Retina Care — Business Card</title>
<link href="https://fonts.googleapis.com/css2?family=Lora:wght@700&family=Poppins:wght@400;500&display=swap" rel="stylesheet">
<style>
  :root {
    --navy: #1d3f6e;
    --navy-deep: #102a4f;
    --blue: #2f5c91;
    --paper: #ffffff;
    --stage: #e9ecf0;
    --ink-light: #ffffff;
  }
  * { box-sizing: border-box; margin: 0; padding: 0; }
  html, body { width: 1200px; height: 913px; overflow: hidden; }
  body {
    background: var(--stage);
    display: flex;
    align-items: center;
    justify-content: center;
    gap: 40px;
    font-family: "Poppins", sans-serif;
  }
  .card {
    width: 540px;
    height: 309px;
    background: var(--paper);
    position: relative;
    overflow: hidden;
    box-shadow: 0 6px 18px rgba(16, 42, 79, 0.18);
  }
  .brand {
    text-align: center;
    font-family: "Poppins", sans-serif;
    font-weight: 500;
    color: var(--navy);
  }
  .card-front .brand { padding-top: 30px; font-size: 15px; }
  .doctor {
    text-align: center;
    margin-top: 22px;
    font-family: "Lora", serif;
    color: var(--navy);
  }
  .doctor-name { font-size: 27px; font-weight: 700; line-height: 1.2; }
  .doctor-title { font-size: 14px; font-weight: 700; margin-top: 4px; color: var(--blue); }
  .contact-band {
    position: absolute;
    left: 0; right: 0; bottom: 0;
    height: 120px;
    background: linear-gradient(100deg, var(--navy-deep) 0%, var(--navy) 60%, var(--blue) 100%);
    color: var(--ink-light);
    padding: 0 30px;
    display: grid;
    grid-template-columns: 1fr 1fr;
    align-content: center;
    row-gap: 10px;
    font-size: 12.5px;
  }
  .contact-item { display: flex; align-items: center; gap: 8px; white-space: nowrap; line-height: 18px; }
  .contact-item.wide { grid-column: 1 / 3; }
  .contact-item svg { width: 18px; height: 18px; flex: none; }
  .card-back { display: flex; align-items: center; justify-content: center; }
  .card-back .brand { font-size: 28px; }
</style>
</head>
<body>
  <section class="card card-front">
    <div class="brand">Silver Birch Retina Care</div>
    <div class="doctor">
      <h1 class="doctor-name">Tobias Rendell , MD , PhD</h1>
      <p class="doctor-title">Board-Certified Vitreoretinal Surgeon</p>
    </div>
    <div class="contact-band">
      <div class="contact-item">
        <svg viewBox="0 0 20 20" fill="none" stroke="currentColor" stroke-width="1.3"><circle cx="10" cy="10" r="9"/><path d="M7 5.5l1.6 2-1 1.2a6 6 0 0 0 3.7 3.7l1.2-1 2 1.6-1 1.5c-3.5 0-7.5-4-7.5-7.5z" fill="currentColor" stroke="none"/></svg>
        617- 482 - 7730
      </div>
      <div class="contact-item">
        <svg viewBox="0 0 20 20" fill="none" stroke="currentColor" stroke-width="1.3"><circle cx="10" cy="10" r="9"/><circle cx="10" cy="10" r="5.5"/><path d="M4.5 10h11M10 4.5c-2 3-2 8 0 11M10 4.5c2 3 2 8 0 11"/></svg>
        www.sbretinahub.example
      </div>
      <div class="contact-item">
        <svg viewBox="0 0 20 20" fill="none" stroke="currentColor" stroke-width="1.3"><circle cx="10" cy="10" r="9"/><rect x="6" y="9" width="8" height="5" rx="0.5"/><path d="M7.5 9V5.5h5V9M7.5 12h5"/></svg>
        617- 391 - 2268
      </div>
      <div class="contact-item">
        <svg viewBox="0 0 20 20" fill="none" stroke="currentColor" stroke-width="1.3"><circle cx="10" cy="10" r="9"/><rect x="5.5" y="6.5" width="9" height="7" rx="0.5"/><path d="M5.5 7l4.5 3.6L14.5 7"/></svg>
        info@sbretinahub.example
      </div>
      <div class="contact-item wide">
        <svg viewBox="0 0 20 20" fill="none" stroke="currentColor" stroke-width="1.3"><circle cx="10" cy="10" r="9"/><path d="M10 15s-3.5-3.6-3.5-6a3.5 3.5 0 0 1 7 0c0 2.4-3.5 6-3.5 6z"/><circle cx="10" cy="9" r="1.2"/></svg>
        87 Larkspur Ave, Suite 210, Fernbrook ME 04412
      </div>
    </div>
  </section>

  <section class="card card-back">
    <div class="brand">Silver Birch Retina Care</div>
  </section>
</body>
</html>
```